Communication Coach needs a business card

https://imgvault-example.net/gallery/1839201/40417/40417_22719043_1839201_8c3e7b2f_preview.png

I like this a lot

I want it to include the following

Delia Strennick
M.A.CCC-SLP
555-204-7718
delia.strennick@mailvento.net
Communication Trainer and Executive Function Coaching
Be Confident-Be Authentic- Be Memorable

on back of card
Public Speaking
Executive Function Coaching
Interview Skills
Corporate Workshops
Self Regulation/Confidence Building

Target Market(s)

adults, parents

Contact Information for Business Card

See above description. i included picture of what i like

Requirements
Must have
• two sides, multi colors ,double sided
Nice to have
• I could have a tag line on front such as Be confident-Be memorable -Be authentic
Should not have
• not too busy or creative as needs to work for corporate setting

```html
<!DOCTYPE html>
<html lang="en">
<head>
<meta charset="utf-8">
<title>Delia Strennick – Business Card</title>
<link rel="stylesheet" href="https://fonts.googleapis.com/css2?family=Lato:wght@400;700;900&display=swap">
<style>
  :root {
    --purple: #8e55a6;
    --yellow: #f5d946;
    --pink: #f1606f;
    --teal: #38b3a8;
    --green: #9bcb4f;
    --ink: #1d1d1f;
    --paper: #ffffff;
    --backdrop: #2b2b2d;
  }
  * { box-sizing: border-box; margin: 0; padding: 0; }
  html, body {
    width: 1200px; height: 900px; overflow: hidden;
    background: var(--backdrop);
    font-family: "Lato", sans-serif;
  }
  .stage {
    width: 1200px; height: 900px;
    display: flex; flex-direction: column; align-items: center; justify-content: center;
    gap: 56px;
  }
  .card {
    width: 580px; height: 332px;
    border-radius: 20px;
    overflow: hidden;
    box-shadow: 0 14px 30px rgba(0,0,0,.45);
  }

  /* Back side */
  .card-back { display: flex; flex-direction: column; }
  .service-band {
    flex: 1;
    display: flex; align-items: center; justify-content: center;
    color: var(--ink);
    font-weight: 900; font-size: 24px; letter-spacing: 2px;
    text-transform: uppercase;
  }
  .band-purple { background: var(--purple); }
  .band-yellow { background: var(--yellow); }
  .band-pink { background: var(--pink); }
  .band-teal { background: var(--teal); }
  .band-green { background: var(--green); }

  /* Front side */
  .card-front {
    background: var(--paper);
    display: flex;
  }
  .edge-stripe { width: 34px; display: flex; flex-direction: column; }
  .edge-stripe span { flex: 1; }
  .front-content {
    flex: 1;
    display: flex; flex-direction: column; align-items: center;
    padding-top: 54px;
    color: var(--ink);
  }
  .holder-name {
    font-weight: 900; font-size: 42px; letter-spacing: 1.5px;
    text-transform: uppercase; line-height: 1;
  }
  .credentials {
    font-size: 22px; letter-spacing: 1.5px; margin-top: 4px;
  }
  .divider {
    width: 40px; height: 3px; background: var(--green);
    margin: 12px 0 12px;
  }
  .phone { font-weight: 700; font-size: 30px; letter-spacing: 1.5px; line-height: 1.1; }
  .email { font-size: 18px; letter-spacing: .5px; margin-top: 4px; }
  .role-pill {
    margin-top: 30px;
    background: var(--ink); color: var(--paper);
    border-radius: 20px;
    padding: 6px 18px;
    font-size: 13px; letter-spacing: 1px; text-transform: uppercase;
  }
  .tagline {
    margin-top: 10px;
    color: var(--purple);
    font-size: 20px; letter-spacing: 1px; text-transform: uppercase;
    display: flex; align-items: center; gap: 6px;
  }
  .tagline strong { font-weight: 900; }
  .dot { width: 7px; height: 7px; border-radius: 50%; display: inline-block; }
  .dot-pink { background: var(--pink); }
  .dot-teal { background: var(--teal); }
</style>
</head>
<body>
<main class="stage">
  <section class="card card-back" aria-label="Card back: services">
    <div class="service-band band-purple">Public Speaking</div>
    <div class="service-band band-yellow">Executive Function Coaching</div>
    <div class="service-band band-pink">Interview Skills</div>
    <div class="service-band band-teal">Corporate Workshops</div>
    <div class="service-band band-green">Self Regulation/Confidence Building</div>
  </section>

  <section class="card card-front" aria-label="Card front: contact">
    <div class="edge-stripe">
      <span class="band-purple"></span><span class="band-yellow"></span><span class="band-pink"></span><span class="band-teal"></span><span class="band-green"></span>
    </div>
    <div class="front-content">
      <h1 class="holder-name">Delia Strennick</h1>
      <p class="credentials">M.A.CCC-SLP</p>
      <div class="divider"></div>
      <p class="phone">555-204-7718</p>
      <p class="email">delia.strennick@mailvento.net</p>
      <p class="role-pill">Communication Trainer &amp; Executive Function Coaching</p>
      <p class="tagline">Be <strong>Confident</strong><span class="dot dot-pink"></span>Be <strong>Authentic</strong><span class="dot dot-teal"></span>Be <strong>Memorable</strong></p>
    </div>
    <div class="edge-stripe">
      <span class="band-purple"></span><span class="band-yellow"></span><span class="band-pink"></span><span class="band-teal"></span><span class="band-green"></span>
    </div>
  </section>
</main>
</body>
</html>
```